Business Card Design for Event Planning Company

Create a business card for event planning company using our new logo. After I pick the design, I will need files made for 6 employees. Our company provides event design & logistics services as well as venue management. The font should be sans serif and complementary to the logo. I will need to know the name of the font selected for the final design. The phone numbers listed should be separated by "." not "-"

Address for the card
PO Box 318, Washington, DC 20019

Card One
Lorna Pettibone
lpettibone@galavoyant.com
202.481.7730

Card Two
Miriam Okonkwo
mokonkwo@galavoyant.com
202.556.2047

Card Three
Tessa Varnholt
tvarnholt@galavoyant.com
978.620.4471

Card Four
Robin Fess
rfess@galavoyant.com
202.718.3362

Card Five
Ada-Rose Pelletan-Uzor
adarose@galavoyant.com
202.839.1205

Card Six
Beatrix Holloway
Beatrix@galavoyant.com
202.492.6618

Target Market(s)

Corporate/Non-Profit

Industry/Entity Type

Event Planning

Contact Information for Business Card

Address for the card

Card One
Lorna Pettibone
lpettibone@galavoyant.com
202.481.7730

Card Two
Miriam Okonkwo
202.556.2047

Card Three
Tessa Varnholt
978.620.4471

Card Four
Robin Fess
rfess@galavoyant.com
202.718.3362

Card Five
Ada-Rose Pelletan-Uzor
202.839.1205

Card Six
Beatrix Holloway
202.492.6618

Font styles to use
Sans Serif

Colors

Designer to choose colors to be used in the design.

Requirements
Must have
• Two-sided with logo
Should not have
• Extra colors or be too busy

```html
<!DOCTYPE html>
<html lang="en">
<head>
<meta charset="utf-8">
<title>Galavoyant Business Card</title>
<link rel="stylesheet" href="https://fonts.googleapis.com/css2?family=Questrial&family=Arimo:wght@400;700&display=swap">
<style>
  :root {
    --backdrop: #2b2b2c;
    --card-dark: #161718;
    --card-light: #f6f6f5;
    --teal: #5ea6a3;
    --ink: #3a3a3a;
    --paper-white: #f4f4f4;
  }
  * { margin: 0; padding: 0; box-sizing: border-box; }
  html, body {
    width: 1200px;
    height: 886px;
    overflow: hidden;
    background: var(--backdrop);
  }
  .canvas {
    position: relative;
    width: 1200px;
    height: 886px;
  }
  .card {
    position: absolute;
    border-radius: 24px;
    box-shadow: 0 14px 30px rgba(0,0,0,0.35);
  }

  /* Front: dark landscape side */
  .card-front {
    left: 70px;
    top: 272px;
    width: 600px;
    height: 343px;
    background: var(--card-dark);
  }
  .brand {
    display: flex;
    align-items: center;
    justify-content: center;
    gap: 14px;
    font-family: "Questrial", sans-serif;
    letter-spacing: 1px;
  }
  .brand-mark {
    border-radius: 50%;
    background: var(--teal);
    flex: none;
  }
  .card-front .brand {
    position: absolute;
    left: 0; right: 0;
    top: 118px;
  }
  .card-front .brand-name {
    font-size: 56px;
    color: var(--paper-white);
  }
  .card-front .brand-mark { width: 22px; height: 22px; }
  .website-line {
    position: absolute;
    left: 0; right: 0;
    top: 252px;
    text-align: center;
    font-family: "Arimo", sans-serif;
    font-size: 14px;
    letter-spacing: 7px;
    color: #d8d8d8;
  }

  /* Back: white portrait side */
  .card-back {
    left: 770px;
    top: 143px;
    width: 343px;
    height: 600px;
    background: var(--card-light);
    text-align: center;
  }
  .card-back .brand {
    position: absolute;
    left: 0; right: 0;
    top: 92px;
    gap: 10px;
  }
  .card-back .brand-name {
    font-size: 42px;
    color: var(--ink);
  }
  .card-back .brand-mark { width: 16px; height: 16px; }

  .contact {
    position: absolute;
    left: 0; right: 0;
    top: 300px;
    font-family: "Arimo", sans-serif;
    color: var(--ink);
    font-size: 15px;
    line-height: 20px;
  }
  .person-name {
    font-weight: 700;
    font-size: 24px;
    line-height: 28px;
    color: var(--teal);
    letter-spacing: -0.3px;
  }
  .divider {
    width: 22px;
    height: 2px;
    background: var(--teal);
    margin: 16px auto;
  }
</style>
</head>
<body>
<main class="canvas">
  <section class="card card-front" aria-label="Card front">
    <div class="brand">
      <span class="brand-mark" aria-hidden="true"></span>
      <span class="brand-name">galavoyant</span>
    </div>
    <p class="website-line">www.galavoyant.com</p>
  </section>

  <section class="card card-back" aria-label="Card back">
    <div class="brand">
      <span class="brand-mark" aria-hidden="true"></span>
      <span class="brand-name">galavoyant</span>
    </div>
    <div class="contact">
      <p class="person-name">Lorna Pettibone</p>
      <div class="divider"></div>
      <p class="address">PO Box 318<br>Washington, DC 20019</p>
      <div class="divider"></div>
      <p class="phone">202.481.7730</p>
      <p class="email">lpettibone@galavoyant.com</p>
      <p class="web">www.galavoyant.com</p>
    </div>
  </section>
</main>
</body>
</html>
```